To create a website for KWRB Accounting and Tax Services

I want to create a website that has a compelling and clean home page, social media connections, some about information, services, pricing and a spot to do simple time bookings and a contact page. I have attached a sample pricing chart, and designs of my logo, business card and letterhead. KWRB Accounting and Tax Services is a small business in beautiful Niagara on the Lake which offers bookkeeping and tax services to the local residents and businesses. I would like the winning design that use the black and blue colour scheme from my stationary and should communicate a professional business that people can trust.

Target Market(s)

local residents who need their taxes prepared as well as small business who need bookkeeping services

Industry/Entity Type

Bookkeeper

Coding

Coded - Design and coding required

Number of Pages Required

5+ page

Font styles to use
Sans Serif

Requirements
Must have
• clean home page with hero images, about section (can be on home page), separate page for services, pricing, time slot booking and contact, social media connections including facebook page, twitter, linkedin,

```html
<!DOCTYPE html>
<html lang="en">
<head>
<meta charset="utf-8">
<title>KWRB Accounting and Tax Services</title>
<link href="https://fonts.googleapis.com/css2?family=Poppins:wght@300;400;600&family=Noto+Serif:wght@400&family=Roboto+Slab:wght@300&family=Roboto:wght@400&family=Roboto+Condensed:wght@700&display=swap" rel="stylesheet">
<style>
:root{
  --topbar:#2d2d2d;
  --header:#3a3a3a;
  --white:#ffffff;
  --orange:#ff6a1a;
  --blue:#0a68ab;
  --cyan-a:#5ccfe9;
  --cyan-b:#74e6f3;
  --section:#f8f8f8;
  --title:#3b3b3b;
  --body:#7a7a7a;
  --rule:#e6e6e6;
}
*{margin:0;padding:0;box-sizing:border-box}
html,body{width:1200px;height:806px;overflow:hidden;background:var(--white)}
.topbar{height:39px;background:var(--topbar);color:var(--white);font:400 10px "Poppins",sans-serif;display:flex;align-items:center;justify-content:space-between;padding:0 164px 0 162px}
.topbar-links{display:flex;gap:13px}
.site-header{height:93px;background:var(--header);display:flex;align-items:center;justify-content:space-between;padding:0 164px 0 162px}
.brand{color:var(--white);font:400 15px/1.3 "Poppins",sans-serif;width:200px}
.main-nav{display:flex;align-items:center}
.main-nav a{color:var(--white);text-decoration:none;font:400 12px "Noto Serif",serif;padding:0 13px;line-height:28px}
.main-nav a.is-cta{background:var(--orange);border-radius:2px;padding:0 14px;margin:0 2px}
.main-nav a:last-child{padding-right:0}
.hero{height:421px;display:flex}
.hero-copy{width:599px;background:linear-gradient(180deg,var(--cyan-a),var(--cyan-b) 45%,var(--cyan-a));color:var(--white);padding:52px 0 0 172px}
.hero-title{font-family:"Poppins",sans-serif;line-height:1}
.hero-title .light{display:block;font-weight:300;font-size:40px;margin-bottom:7px}
.hero-title .bold{display:block;font-weight:600;font-size:43px;letter-spacing:1px;margin-bottom:7px}
.hero-lead{font:400 16px/19px "Noto Serif",serif;margin-top:32px;width:420px;white-space:nowrap}
.hero-actions{display:flex;gap:13px;margin-top:50px}
.btn{display:inline-flex;align-items:center;justify-content:center;width:156px;height:37px;color:var(--white);text-decoration:none;font:400 13px "Poppins",sans-serif;border-radius:2px}
.btn-blue{background:var(--blue)}
.btn-orange{background:var(--orange)}
.hero-photo{flex:1;background:linear-gradient(100deg,#c9c4c0 0%,#e9e6e2 40%,#a8aaac 75%,#8e9092 100%)}
.features{height:248px;background:var(--section);border-bottom:1px solid var(--rule);display:flex;padding:54px 0 0 237px}
.feature{width:189px}
.feature-head{display:flex;gap:8px;align-items:flex-start;height:36px}
.feature-icon{width:28px;height:30px;flex:none;margin-top:1px}
.feature-title{font:300 16px/18px "Roboto Slab",serif;color:var(--title);white-space:nowrap}
.feature-text{font:400 9px/12.5px "Roboto",sans-serif;color:var(--body);margin-top:16px;width:160px;height:38px}
.read-more{display:inline-flex;align-items:center;justify-content:center;width:79px;height:31px;margin-top:15px;background:var(--orange);color:var(--white);text-decoration:none;font:700 11px "Roboto Condensed",sans-serif;border-radius:2px}
</style>
</head>
<body>
<div class="topbar">
  <span class="topbar-address">1234 Orchard Road, Fairhaven, 00000</span>
  <nav class="topbar-links"><span>Cart £0.00</span><span>|</span><span>Register</span><span>|</span><span>Client login</span></nav>
</div>
<header class="site-header">
  <div class="brand">KWRB Accounting and Tax Services</div>
  <nav class="main-nav">
    <a href="#">Home</a><a href="#">About</a><a href="#">Services</a><a href="#">Pricing</a><a href="#">Blog</a><a href="#" class="is-cta">Appointment</a><a href="#">Contact</a>
  </nav>
</header>
<section class="hero">
  <div class="hero-copy">
    <h1 class="hero-title"><span class="light">Professional</span><span class="bold">TAX / BUSINESS</span><span class="light">Service</span></h1>
    <p class="hero-lead">Our courses are built in partnerships with technology<br>leaders and are relevant to industry needs.</p>
    <div class="hero-actions"><a href="#" class="btn btn-blue">Free Consulation</a><a href="#" class="btn btn-orange">More About Us</a></div>
  </div>
  <div class="hero-photo" role="img" aria-label="Businessman in a grey suit with arms crossed, colleagues at a meeting table behind him"></div>
</section>
<section class="features">
  <article class="feature">
    <div class="feature-head">
      <svg class="feature-icon" viewBox="0 0 28 30" role="img" aria-label="Tax preparer icon"><circle cx="14" cy="10" r="8" fill="#d93b32"/><rect x="2" y="20" width="24" height="9" rx="4" fill="#c7302a"/></svg>
      <h2 class="feature-title">Check Status Of<br>Your Return</h2>
    </div>
    <p class="feature-text">We are ready to provide you with up-to-date refund information online, by phone, or during personal meeting</p>
    <a href="#" class="read-more">READ MORE</a>
  </article>
  <article class="feature">
    <div class="feature-head">
      <svg class="feature-icon" viewBox="0 0 28 30" role="img" aria-label="Calculator icon"><rect x="4" y="1" width="20" height="28" rx="3" fill="#5a5f73"/><rect x="7" y="5" width="14" height="18" fill="#dfe8ee"/><rect x="9" y="8" width="10" height="2" fill="#39a96b"/><rect x="9" y="12" width="10" height="2" fill="#8fa0ad"/><rect x="9" y="16" width="10" height="2" fill="#8fa0ad"/></svg>
      <h2 class="feature-title">Withholding<br>Calculator</h2>
    </div>
    <p class="feature-text">If you are an employee, you can apply for help to decide whether you need to give your employer a new form W-4</p>
    <a href="#" class="read-more">READ MORE</a>
  </article>
  <article class="feature">
    <div class="feature-head">
      <svg class="feature-icon" viewBox="0 0 28 30" role="img" aria-label="House icon"><path d="M1 14 14 3l13 11z" fill="#d63a33"/><rect x="4" y="14" width="20" height="14" fill="#e9dcc9"/><rect x="7" y="18" width="5" height="10" fill="#7a5336"/><rect x="16" y="17" width="5" height="5" fill="#6f8fb3"/></svg>
      <h2 class="feature-title">Property<br>Taxes</h2>
    </div>
    <p class="feature-text">If you need help paying property tax, wish to apply for a property tax refund etc., our tax specialists are here for you</p>
    <a href="#" class="read-more">READ MORE</a>
  </article>
  <article class="feature">
    <div class="feature-head">
      <svg class="feature-icon" viewBox="0 0 28 30" role="img" aria-label="Bank building icon"><path d="M1 10 14 2l13 8z" fill="#9b9b9b"/><rect x="2" y="10" width="24" height="3" fill="#b5b5b5"/><rect x="5" y="14" width="3" height="11" fill="#a6a6a6"/><rect x="12.5" y="14" width="3" height="11" fill="#a6a6a6"/><rect x="20" y="14" width="3" height="11" fill="#a6a6a6"/><rect x="2" y="25" width="24" height="4" fill="#8d8d8d"/></svg>
      <h2 class="feature-title">Own a<br>Business?</h2>
    </div>
    <p class="feature-text">As a business owner, you must know all tax pitfalls, that's why our business planning department is working for you</p>
    <a href="#" class="read-more">READ MORE</a>
  </article>
</section>
</body>
</html>
```